Pyschiatry Experts need Marketing Campaign

Ad(s) developed for print advertising sharing our purpose and services, highlighting our medical care providers. Must be welcoming and inviting while displaying a high level of professionalism expected from a physician's office.

Target Market(s)

Local community

Industry/Entity Type

Psychiatry (Healthcare)

Requirements
Must have
• Staff pictures, 'Medication Management Experts', 'Prompt Appointments', 'ADD/ADHD, Bipolar Disorder, Depression, Anxiety, Schizophrenia, Grief Reaction and others' 'Virtual and In-Person Visits'
Nice to have
• Address: 412 E Marlowe Coeur d'Alene Phone (208)555-7813 website: BrightKestrel.example Hours: Mon - Thur 7am - 6pm

```html
<!DOCTYPE html>
<html lang="en">
<head>
<meta charset="utf-8">
<title>Meridian Crest Health – Print Ad</title>
<link rel="stylesheet" href="https://fonts.googleapis.com/css2?family=Encode+Sans+Condensed:wght@400;700;800&family=Montserrat:wght@400;500;600;700&display=swap">
<style>
  :root{
    --stage:#3a9b94;
    --paper:#ffffff;
    --teal:#10b8ad;
    --teal-deep:#1b8f86;
    --forest:#1f4f3d;
    --footer:#244d3e;
    --lime:#a6d05a;
    --sky:#dbeefa;
    --sky-pale:#e6f4fb;
    --ink:#1c2b26;
  }
  *{box-sizing:border-box;margin:0;padding:0}
  html,body{width:1200px;height:1200px;overflow:hidden;background:var(--stage)}
  .flyer{position:absolute;left:157px;top:26px;width:886px;height:1148px;background:var(--paper);overflow:hidden;font-family:"Montserrat",sans-serif;color:var(--ink)}
  .abs{position:absolute}

  .hero-art{left:0;top:0;width:886px;height:515px}

  .brand{left:0;top:60px;width:420px;text-align:center}
  .brand-mark{display:block;margin:0 auto 18px;width:74px;height:74px;border-radius:50%;background:var(--teal)}
  .brand-name{font-family:"Encode Sans Condensed",sans-serif;font-weight:700;font-size:30px;color:var(--teal);letter-spacing:1px;text-transform:uppercase}

  .headline{left:65px;top:243px;font-family:"Encode Sans Condensed",sans-serif;font-weight:800;font-size:50px;line-height:60px}
  .headline .lead{color:var(--teal)}
  .headline .key{color:var(--forest)}

  .services{left:65px;top:438px;font-family:"Encode Sans Condensed",sans-serif;font-weight:400;font-size:22px;line-height:28px;color:var(--forest)}

  .providers-title{left:0;top:530px;width:886px;text-align:center;font-family:"Encode Sans Condensed",sans-serif;font-weight:800;font-size:34px;color:var(--forest)}
  .providers-intro{left:90px;top:576px;width:706px;text-align:center;font-size:13.5px;line-height:17.5px}

  .team-band{left:0;top:860px;width:886px;height:0}
  .team-art{left:0;top:640px;width:886px;height:250px}

  .provider{top:829px;width:170px;text-align:center;color:#fff}
  .provider-name{font-weight:600;font-size:17px;line-height:20px}
  .provider-cred{font-weight:400;font-size:14px;line-height:18px}

  .migraine{left:0;top:886px;width:886px;height:107px;background:var(--sky);padding:12px 110px 0;text-align:center;font-size:13.5px;line-height:17.5px}

  .offer-row{left:0;top:993px;width:626px;height:50px;border:1.5px solid var(--forest);border-left:none;border-radius:0 25px 25px 0;background:#fff;display:flex;align-items:center;padding-left:38px;gap:8px;font-size:13.5px;color:var(--forest)}
  .offer-row span::before{content:"";display:inline-block;width:7px;height:7px;border-radius:50%;background:var(--forest);margin-right:5px;vertical-align:1px}
  .hours{left:629px;top:993px;width:257px;height:50px;background:var(--lime);border-radius:25px 0 0 25px;display:flex;align-items:center;justify-content:center;font-family:"Encode Sans Condensed",sans-serif;font-weight:700;font-size:19px;color:var(--forest)}
  .gap-strip{left:0;top:1043px;width:886px;height:12px;background:var(--sky)}

  .footer{left:0;top:1055px;width:886px;height:93px;background:var(--footer);color:#fff}
  .footer-divider{top:8px;width:1px;height:77px;background:var(--teal-deep)}
  .footer-item{top:0;height:93px;display:flex;align-items:center;gap:14px}
  .address{font-size:14px;line-height:18px}
  .address b{font-weight:600}
  .phone{font-weight:700;font-size:25px}
  .web{font-size:14.5px}
</style>
</head>
<body>
<main class="flyer">

  <svg class="abs hero-art" viewBox="0 0 886 515" aria-hidden="false">
    <defs>
      <linearGradient id="room" x1="0" y1="0" x2="1" y2="1">
        <stop offset="0" stop-color="#e9f2f6"/>
        <stop offset="0.45" stop-color="#c9b49e"/>
        <stop offset="0.75" stop-color="#c98a2e"/>
        <stop offset="1" stop-color="#d9d6d2"/>
      </linearGradient>
    </defs>
    <path d="M462 0 C380 120 375 360 440 515 L886 515 L886 0 Z" fill="#bfe3e2"/>
    <path d="M478 0 C395 130 395 370 455 515 L886 515 L886 0 Z" fill="url(#room)" role="img" aria-label="Photo: smiling woman on a sofa working on a laptop in a bright living room"/>
  </svg>

  <div class="abs brand">
    <span class="brand-mark"></span>
    <span class="brand-name">Meridian Crest Health</span>
  </div>

  <h1 class="abs headline">
    <span class="lead">Helping</span> <span class="key">Bodies</span><br>
    <span class="lead">Helping</span> <span class="key">Minds</span><br>
    <span class="lead">Helping</span> <span class="key">You</span>
  </h1>

  <p class="abs services">Mental Health and Psychiatry Services<br>Migraine and Neurospasticity Intervention</p>

  <h2 class="abs providers-title">Meet Our Mental Health Providers</h2>
  <p class="abs providers-intro">Bringing comprehensive evaluation, medication management and psychotherapy to the full spectrum of mental health disorders including minor, moderate and major depression, bipolar disorder, ADD/ADHD, anxiety, schizophrenia, stress or grief reactions, and others.</p>

  <svg class="abs team-art" viewBox="0 0 886 250">
    <path d="M0 78 Q120 62 200 60 L686 60 Q780 62 886 72 L886 93 L0 93 Z" fill="var(--sky-pale)"/>
    <rect x="0" y="93" width="886" height="154" fill="var(--teal)"/>
    <g>
      <circle cx="180" cy="93" r="90" fill="var(--sky-pale)"/>
      <circle cx="180" cy="93" r="80" fill="var(--lime)"/>
      <circle cx="180" cy="93" r="75" fill="var(--teal-deep)"/>
      <circle cx="180" cy="93" r="69" fill="#8d969c" role="img" aria-label="Portrait photo of provider Owen Talbright"/>
    </g>
    <g>
      <circle cx="355" cy="93" r="90" fill="var(--sky-pale)"/>
      <circle cx="355" cy="93" r="80" fill="var(--lime)"/>
      <circle cx="355" cy="93" r="75" fill="var(--teal-deep)"/>
      <circle cx="355" cy="93" r="69" fill="#868e94" role="img" aria-label="Portrait photo of provider Marla Dunsworth"/>
    </g>
    <g>
      <circle cx="530" cy="93" r="90" fill="var(--sky-pale)"/>
      <circle cx="530" cy="93" r="80" fill="var(--lime)"/>
      <circle cx="530" cy="93" r="75" fill="var(--teal-deep)"/>
      <circle cx="530" cy="93" r="69" fill="#7f8a92" role="img" aria-label="Portrait photo of provider Glen Ashcombe"/>
    </g>
    <g>
      <circle cx="705" cy="93" r="90" fill="var(--sky-pale)"/>
      <circle cx="705" cy="93" r="80" fill="var(--lime)"/>
      <circle cx="705" cy="93" r="75" fill="var(--teal-deep)"/>
      <circle cx="705" cy="93" r="69" fill="#8a9196" role="img" aria-label="Portrait photo of provider Ruth Pellerin"/>
    </g>
  </svg>

  <div class="abs provider" style="left:95px"><div class="provider-name">Owen Talbright</div><div class="provider-cred">PMHNP - BC</div></div>
  <div class="abs provider" style="left:270px"><div class="provider-name">Marla Dunsworth</div><div class="provider-cred">PMHNP - BC</div></div>
  <div class="abs provider" style="left:445px"><div class="provider-name">Glen Ashcombe</div><div class="provider-cred">PMHNP - BC</div></div>
  <div class="abs provider" style="left:620px"><div class="provider-name">Ruth Pellerin</div><div class="provider-cred">PMHNP-BC, DNP</div></div>

  <p class="abs migraine">Migraine management and intervention can be a complex journey. Identifying food and environmental triggers, identification of migraine type, pharmacological management with a new generation of highly effective medications and/or botulinum injections are all part of our comprehensive care program for migraine sufferers.</p>

  <div class="abs offer-row">
    <span>New Patient Evaluation</span>
    <span>Insurance Pre-Authorization</span>
    <span>Follow-Up Appointments</span>
  </div>
  <div class="abs hours">Hours: Mon - Thur 7am - 6pm</div>
  <div class="abs gap-strip"></div>

  <footer class="abs footer">
    <div class="abs footer-item" style="left:30px">
      <svg width="22" height="30" viewBox="0 0 22 30"><path d="M11 0C5 0 0 5 0 11c0 8 11 19 11 19s11-11 11-19C22 5 17 0 11 0z" fill="var(--lime)"/><circle cx="11" cy="11" r="4.5" fill="var(--footer)"/></svg>
      <div class="address"><b>Meridian Crest Health</b><br>412 E Marlowe Coeur d'Alene</div>
    </div>
    <div class="abs footer-divider" style="left:306px"></div>
    <div class="abs footer-item" style="left:340px">
      <svg width="30" height="30" viewBox="0 0 30 30"><circle cx="15" cy="15" r="15" fill="var(--lime)"/><path d="M10.5 7.5l3 3.2-1.6 2.1c.9 2 2.4 3.5 4.3 4.4l2.1-1.6 3.2 3-1.6 2.6c-5.9-.3-11-5.4-11.3-11.3z" fill="var(--footer)"/></svg>
      <div class="phone">(208)555-7813</div>
    </div>
    <div class="abs footer-divider" style="left:618px"></div>
    <div class="abs footer-item" style="left:660px">
      <svg width="30" height="30" viewBox="0 0 30 30" fill="none" stroke="var(--lime)" stroke-width="2"><circle cx="15" cy="15" r="13"/><ellipse cx="15" cy="15" rx="6" ry="13"/><path d="M2 15h26M4.5 8h21M4.5 22h21"/></svg>
      <div class="web">BrightKestrel.example</div>
    </div>
  </footer>

</main>
</body>
</html>
```